Post Card Design - Photo on front, details on back. Logo on both sides.

Back: See the photo of my old card. The back worked well, as it gave me lots of space to write on. The address details are still correct, but the logo has changed to Josephine Sans. Logo can be on one line or on two (if two, align it on the left).
Don't include the 'BEAUTIFUL WEDDING DRESSES...' bit.
I'd like to print this on thicker, slightly coarse paper, so don't go too small on detail.
Here are the Plume paper details: Paper Stock: Natural Uncoated
Paper Thickness: Premium
Finish: None
Front of Card: I'd like to see options for both pictures:
I think the painted image would look best with a frame in a pale shade and the logo in the frame fairly subtle.
The actual dress photo I'd like to see cropped a bit like in my mock up. You'll need to have a look at how the logo would be best placed on this. You can place it anywhere, or add a banner.
See my website for my brand's look: mirabeltoft.co.nz
Target Market(s)
Brides
Industry/Entity Type
Wedding Dresses
Contact Information for Business Card
Front: Photo and logo. Back: with details and lots of empty space. See attached photos for loose brief.
Other font styles liked:
- Josephine Sans
Requirements
Must have
- I hand-write the gown designs and price on the back of the card, so there needs to be plenty of empty space.
Nice to have
- As per brief.
Should not have
- It must look clean, romantic, modern. Timeless.

```html
<!DOCTYPE html>
<html lang="en">
<head>
<meta charset="utf-8">
<title>Mirabel Toft — Post Card</title>
<link href="https://fonts.googleapis.com/css2?family=Josefin+Sans:wght@400;600&display=swap" rel="stylesheet">
<style>
:root{
  --backdrop-light:#ececec;
  --backdrop-dark:#9c9c9c;
  --ink:#111111;
  --paper:#ffffff;
  --cream:#f1d89c;
  --cream-deep:#e8c98a;
  --stone:#d9c19a;
  --stone-dark:#8a6a4a;
  --blush:#f0a4a0;
  --rose:#e0707a;
  --banner:rgba(190,160,100,.32);
  --haze:#e9e9e9;
}
*{margin:0;padding:0;box-sizing:border-box}
html,body{width:1200px;height:1200px;overflow:hidden}
body{
  background:linear-gradient(135deg,var(--backdrop-light) 0%,var(--backdrop-dark) 100%);
  font-family:"Josefin Sans",sans-serif;
  color:var(--ink);
  position:relative;
}
.card{position:absolute;left:272px;width:656px;height:437px;overflow:hidden}
.card--front{top:129px;background:var(--cream)}
.card--back{top:634px;background:var(--paper)}

/* front */
.front-photo{
  position:absolute;left:0;top:0;width:250px;height:437px;
  background:
    linear-gradient(90deg,rgba(241,216,156,0) 70%,var(--cream) 100%),
    linear-gradient(180deg,#efe0c4 0%,#e6cfa6 45%,#c8a27a 80%,#b48a66 100%);
}
.front-painting{
  position:absolute;left:262px;top:14px;width:340px;height:410px;
  border-radius:46% 46% 40% 40%;
  background:
    radial-gradient(ellipse at 35% 65%,var(--rose) 0%,var(--blush) 30%,rgba(240,164,160,0) 60%),
    radial-gradient(ellipse at 70% 45%,#f7efd8 0%,rgba(247,239,216,0) 45%),
    radial-gradient(ellipse at 50% 50%,#f3c3a8 0%,rgba(241,216,156,0) 72%);
}
.front-banner{
  position:absolute;left:0;top:197px;width:656px;height:64px;
  background:var(--banner);
}
.front-name{
  position:absolute;left:73px;top:213px;
  font-size:24px;font-weight:400;letter-spacing:.06em;
  white-space:nowrap;
}

/* back */
.back-photo{
  position:absolute;right:0;top:0;width:260px;height:437px;
  background:
    linear-gradient(90deg,var(--paper) 0%,rgba(255,255,255,0) 45%),
    linear-gradient(180deg,var(--haze) 0%,#f2f2f2 60%,#f7f7f7 100%);
}
.back-name{
  position:absolute;left:43px;top:271px;
  font-size:28px;font-weight:400;line-height:1.02;letter-spacing:.04em;
}
.back-rule{
  position:absolute;left:45px;top:341px;width:565px;height:2px;background:var(--ink);
}
.contact{position:absolute;left:45px;top:355px;list-style:none}
.contact li{display:flex;align-items:center;gap:8px;height:16px;letter-spacing:.04em}
.contact svg{width:9px;height:9px;flex:none}
.contact .phone{font-size:14px;font-weight:600;height:20px}
.contact .small{font-size:10px}
.social-handle{
  position:absolute;right:47px;top:388px;
  font-size:11px;font-weight:400;letter-spacing:.04em;color:#333;
}
</style>
</head>
<body>

<section class="card card--front">
  <div class="front-photo" role="img" aria-label="Photograph of a bride in an off-shoulder fitted gown with long train, standing in a sunlit stone colonnade"></div>
  <div class="front-painting" role="img" aria-label="Vintage painted illustration of an embracing couple surrounded by pink and peach flowers"></div>
  <div class="front-banner"></div>
  <h1 class="front-name">MIRABEL TOFT</h1>
</section>

<section class="card card--back">
  <div class="back-photo" role="img" aria-label="Faded greyscale photograph of the bride in her gown"></div>
  <h2 class="back-name">MIRABEL<br>TOFT</h2>
  <div class="back-rule"></div>
  <ul class="contact">
    <li class="phone">
      <svg viewBox="0 0 10 10"><path d="M2 1 L3.6 1 L4.2 3 L3.2 3.8 Q4 5.8 6.2 6.8 L7 5.8 L9 6.4 L9 8 Q8.6 9 7.6 9 Q1 8.4 1 2.4 Q1 1 2 1Z" fill="var(--ink)"/></svg>
      +64 9 555 0147
    </li>
    <li class="small">
      <svg viewBox="0 0 10 10"><rect x="1" y="2" width="8" height="6" fill="var(--ink)"/><path d="M1 2 L5 5.4 L9 2" stroke="var(--paper)" stroke-width=".8" fill="none"/></svg>
      HELLO@MIRABELTOFT.CO.NZ
    </li>
    <li class="small">
      <svg viewBox="0 0 10 10"><circle cx="5" cy="5" r="4" fill="none" stroke="var(--ink)" stroke-width="1.2"/><ellipse cx="5" cy="5" rx="1.6" ry="4" fill="none" stroke="var(--ink)" stroke-width=".8"/><line x1="1" y1="5" x2="9" y2="5" stroke="var(--ink)" stroke-width=".8"/></svg>
      MIRABELTOFT.CO.NZ
    </li>
  </ul>
  <p class="social-handle">@mirabeltoft</p>
</section>

</body>
</html>
```